Narvelo - Human Capital Consultancy Business Cards

We need a business card design for a new professional services consulting company which is focused on People, Performance, Profit. Hence the company name "Narvelo Pty Ltd". We intend to work with organisations predominantly on achieving optimal business performance through it's people. Developing both individual and organisational capability through effective learning and talent management strategies. We also plan to offer leadership programs which look at how people can utilise wellness, mindfulness and resilience to enable them and their teams to perform more effectively. We are looking for something quite dynamic, even sporty looking rather than a staid'professional services' look. Please see logo attached.

Leadership

```html
<!DOCTYPE html>
<html lang="en">
<head>
<meta charset="utf-8">
<title>Narvelo Business Cards</title>
<link rel="stylesheet" href="https://fonts.googleapis.com/css2?family=Didact+Gothic&family=Montserrat:wght@600;700&family=PT+Sans&display=swap">
<style>
  :root {
    --backdrop: #e4e5e7;
    --paper: #f7f7f6;
    --navy: #2b3190;
    --royal: #2a5fae;
    --cyan: #24a3d6;
    --orange: #e07b1e;
    --ink: #3c3c3e;
    --ink-soft: #5f6064;
    --icon-blue: #3f6ea8;
  }
  * { box-sizing: border-box; margin: 0; padding: 0; }
  html, body { width: 1200px; height: 1200px; overflow: hidden; }
  body {
    background: var(--backdrop);
    display: flex;
    flex-direction: column;
    align-items: center;
    justify-content: center;
    gap: 60px;
  }
  .card {
    width: 880px;
    height: 538px;
    position: relative;
    overflow: hidden;
    box-shadow: 0 6px 18px rgba(0,0,0,0.12);
  }

  /* Front */
  .card-front {
    background: linear-gradient(120deg, var(--cyan) 0%, var(--royal) 45%, var(--navy) 100%);
    display: flex;
    flex-direction: column;
    align-items: center;
    justify-content: center;
    gap: 26px;
    color: #fff;
  }
  .wordmark {
    font-family: "Montserrat", sans-serif;
    font-weight: 700;
    font-size: 84px;
    letter-spacing: 1px;
    line-height: 1;
  }
  .tagline {
    font-family: "PT Sans", sans-serif;
    font-size: 30px;
    letter-spacing: 0.5px;
  }
  .tagline .sep { padding: 0 6px; }

  /* Back */
  .card-back { background: var(--paper); }
  .holder {
    position: absolute;
    top: 58px; left: 360px;
    font-family: "Montserrat", sans-serif;
    font-size: 48px;
    color: var(--ink);
  }
  .holder-name { font-weight: 700; font-style: italic; letter-spacing: -0.5px; }
  .holder-title { font-family: "Didact Gothic", sans-serif; font-weight: 400; color: var(--ink-soft); margin-left: 6px; }

  .brand {
    position: absolute;
    top: 168px; left: 40px;
    width: 320px;
    display: flex;
    flex-direction: column;
    align-items: center;
    gap: 18px;
  }
  .brand .wordmark { color: var(--navy); font-size: 52px; }
  .brand .tagline { color: var(--ink); font-size: 17px; }
  .brand .tagline .sep { padding: 0 3px; }

  .contacts {
    position: absolute;
    top: 170px; left: 400px;
    list-style: none;
    font-family: "Didact Gothic", sans-serif;
    font-size: 27px;
    color: var(--ink-soft);
    display: flex;
    flex-direction: column;
    gap: 12px;
  }
  .contacts li { display: flex; align-items: center; gap: 18px; }
  .contact-icon { width: 34px; height: 34px; flex: none; }

  .bands { position: absolute; left: 0; bottom: 0; width: 880px; height: 120px; }
</style>
</head>
<body>

  <section class="card card-front" aria-label="Card front">
    <div class="wordmark">Narvelo</div>
    <p class="tagline">Capability<span class="sep">•</span>Wellness<span class="sep">•</span>Growth</p>
  </section>

  <section class="card card-back" aria-label="Card back">
    <h1 class="holder"><span class="holder-name">FirstLast</span><span class="holder-title">title</span></h1>

    <div class="brand">
      <div class="wordmark">Narvelo</div>
      <p class="tagline">Capability<span class="sep">•</span>Wellness<span class="sep">•</span>Growth</p>
    </div>

    <ul class="contacts">
      <li>
        <svg class="contact-icon" viewBox="0 0 34 34" aria-hidden="true">
          <circle cx="17" cy="17" r="16" fill="#eeeeee"/>
          <path d="M12 9 q-3 2 -1 8 q3 7 9 9 q3 1 4 -1 l-3 -3 q-2 1 -3 0 q-3 -2 -4 -5 q0 -2 1 -2 z" fill="var(--orange)"/>
        </svg>
        <span>001 101 10 01</span>
      </li>
      <li>
        <svg class="contact-icon" viewBox="0 0 34 34" aria-hidden="true">
          <circle cx="17" cy="17" r="16" fill="var(--icon-blue)"/>
          <rect x="9" y="11" width="16" height="12" fill="#fff"/>
          <path d="M9 11 L17 18 L25 11" fill="none" stroke="var(--icon-blue)" stroke-width="1.5"/>
        </svg>
        <span>name@server.com.au</span>
      </li>
      <li>
        <svg class="contact-icon" viewBox="0 0 34 34" aria-hidden="true">
          <circle cx="17" cy="17" r="16" fill="var(--cyan)"/>
        </svg>
        <span>@socialname</span>
      </li>
      <li>
        <svg class="contact-icon" viewBox="0 0 34 34" aria-hidden="true">
          <circle cx="17" cy="17" r="16" fill="var(--icon-blue)"/>
          <rect x="9" y="10" width="16" height="11" fill="#fff"/>
          <rect x="15" y="21" width="4" height="3" fill="#fff"/>
          <rect x="12" y="24" width="10" height="2" fill="#fff"/>
        </svg>
        <span>www.server.com.au</span>
      </li>
    </ul>

    <svg class="bands" viewBox="0 0 880 120" preserveAspectRatio="none" aria-hidden="true">
      <polygon points="0,0 220,0 170,120 0,120" fill="var(--navy)"/>
      <polygon points="150,40 640,40 600,120 118,120" fill="var(--orange)"/>
      <polygon points="620,72 880,72 880,120 600,120" fill="var(--cyan)"/>
    </svg>
  </section>

</body>
</html>
```